Nature and Scenic Photographs Business Card Design

I require a simple business card using the illustration that I have provided

Industry/Entity Type

Business

Contact Information for Business Card

Gil Harlow
Mobile: 0436182057
Skype: gilbert.moray.harlow

```html
<!DOCTYPE html>
<html lang="en">
<head>
<meta charset="utf-8">
<title>Gil Harlow – Photographer Business Card</title>
<link href="https://fonts.googleapis.com/css2?family=Almendra:wght@400;700&display=swap" rel="stylesheet">
<style>
  :root {
    --page-bg: #2a2a2a;
    --card-bg: #0b0b0b;
    --ink-green: #86c47a;
    --forest-shadow: #0f160b;
    --forest-dark: #1c2813;
    --forest-mid: #3a5322;
    --forest-moss: #5f7f2c;
    --forest-light: #a9be7a;
  }
  * { margin: 0; padding: 0; box-sizing: border-box; }
  html, body {
    width: 1200px;
    height: 1000px;
    overflow: hidden;
    background: var(--page-bg);
  }
  .business-card {
    position: absolute;
    left: 100px;
    top: 210px;
    width: 1000px;
    height: 580px;
    background: var(--card-bg);
    box-shadow: 0 20px 50px rgba(0,0,0,0.55);
  }
  .forest-photo {
    position: absolute;
    left: 24px;
    top: 24px;
    width: 580px;
    height: 532px;
    background:
      radial-gradient(ellipse 30% 22% at 70% 8%, rgba(200,215,150,0.55), transparent 70%),
      radial-gradient(ellipse 22% 40% at 45% 30%, rgba(20,30,12,0.7), transparent 70%),
      radial-gradient(ellipse 35% 30% at 18% 28%, rgba(110,150,70,0.6), transparent 70%),
      radial-gradient(ellipse 60% 14% at 55% 74%, rgba(110,145,45,0.85), transparent 75%),
      radial-gradient(ellipse 40% 10% at 70% 60%, rgba(95,127,44,0.7), transparent 75%),
      radial-gradient(ellipse 50% 18% at 40% 92%, rgba(70,55,35,0.75), transparent 75%),
      radial-gradient(ellipse 18% 20% at 95% 88%, rgba(170,200,110,0.6), transparent 70%),
      linear-gradient(180deg, var(--forest-mid) 0%, var(--forest-dark) 45%, var(--forest-mid) 70%, var(--forest-shadow) 100%);
  }
  .card-details {
    position: absolute;
    left: 604px;
    top: 0;
    width: 396px;
    height: 580px;
    color: var(--ink-green);
    font-family: "Almendra", serif;
    text-align: center;
  }
  .owner-name {
    position: absolute;
    top: 88px;
    width: 100%;
    font-size: 60px;
    font-weight: 400;
    line-height: 1;
  }
  .owner-role {
    position: absolute;
    top: 152px;
    width: 100%;
    font-size: 32px;
    line-height: 1;
  }
  .contact-list {
    position: absolute;
    top: 284px;
    width: 100%;
    list-style: none;
  }
  .contact-list li {
    font-size: 27px;
    line-height: 50px;
    white-space: nowrap;
  }
  .contact-list .contact-mobile { font-size: 32px; }
</style>
</head>
<body>
  <div class="business-card">
    <div class="forest-photo" role="img" aria-label="Rainforest photograph: mossy fallen logs, ferns and palms under tall trees with light through the canopy"></div>
    <div class="card-details">
      <h1 class="owner-name">Gil Harlow</h1>
      <p class="owner-role">Photographer</p>
      <ul class="contact-list">
        <li class="contact-mobile">Mobile: 0436182057</li>
        <li class="contact-email">Email: gil.mor4@fernpost.com</li>
        <li class="contact-skype">Skype: gilbert.moray.harlow</li>
      </ul>
    </div>
  </div>
</body>
</html>
```